Capability statement for an Electrical Business based in Sydney Australia

The aim for the Capability statement is for us to look more professional when we meet someone or after cold calling and have to send them our business details.
Need something simple, efficient and to the point.

It should have the following content
- Our mission (details can be as attached PDF)
- Areas we service (this can be a google map of areas we service but basically the areas are
Metro Sydney with our work centralised around the Norwest, Hills, Inner west and Epping area)
- List of services we provide (as PDF)
- Details about us; who we are, contact details, licenses (as PDF)
- Why they should choose us
(As pdf)

Right now, we're just after a nice format we're happy with, the details we are happy to provide with once we have a design in mind.

I've attached our current existing capability statement and what our details are. Also, our website is
https://brightwirepro.com.au/

Thanks in advance!

Requirements
Should not have
• Should not be complicated for the reader

```html
<!DOCTYPE html>
<html lang="en">
<head>
<meta charset="utf-8">
<title>BrightWire Pro – Capabilities Statement</title>
<link href="https://fonts.googleapis.com/css2?family=Heebo:wght@300;400;500;700;800&display=swap" rel="stylesheet">
<style>
  :root{
    --red:#b8382f;
    --red-text:#c9443a;
    --black:#1b1b1b;
    --white:#ffffff;
    --ink:#262626;
    --pale:#f3d3ce;
    --backdrop:#cdd1d4;
  }
  *{box-sizing:border-box;margin:0;padding:0}
  html,body{width:1057px;height:1200px;overflow:hidden}
  body{background:var(--backdrop);font-family:'Heebo',sans-serif;color:var(--ink);position:relative}
  .sheet{position:absolute;left:102px;top:0;width:852px;height:1200px;background:var(--white);overflow:hidden}
  .block{position:absolute}

  /* header */
  .hero-photo{left:290px;top:0;width:562px;height:293px;
    background:radial-gradient(circle at 68% 55%,#8a6a3c 0,#3b3f4a 22%,#22262e 55%,#15171c 100%)}
  .hero-shapes{left:0;top:0;width:852px;height:390px}
  .statement-title{left:372px;top:318px;font-size:35px;font-weight:400;color:var(--ink);letter-spacing:.2px;line-height:1}
  .statement-title strong{color:var(--red);font-weight:800}

  .brand{left:30px;top:36px;width:250px}
  .brand-name{display:flex;align-items:center;gap:10px;font-size:31px;font-weight:800;color:var(--red);line-height:1}
  .brand-dot{width:18px;height:18px;border-radius:50%;background:var(--red);flex:none}
  .brand-rule{margin-top:26px;height:2px;width:246px;background:linear-gradient(90deg,var(--white) 0 50%,var(--red) 50% 100%)}

  .intro{left:30px;width:300px;color:var(--white)}
  .intro.mission{top:144px}
  .intro.values{top:250px}
  .section-head{display:flex;align-items:center;gap:12px;font-size:19px;font-weight:700;line-height:1}
  .section-head em{font-style:normal;color:var(--red-text)}
  .intro p{margin-top:17px;font-size:13.4px;line-height:17.5px}
  .values p{margin-top:20px}

  .icon{width:20px;height:20px;border-radius:50%;background:var(--red);flex:none;display:inline-flex;align-items:center;justify-content:center}
  .icon::after{content:"";width:8px;height:8px;border:1.5px solid var(--white);border-radius:50%}

  /* who we are */
  .who{left:0;top:387px;width:423px;height:230px;background:var(--red);padding:18px 30px 0}
  .who .section-head{color:var(--ink);font-size:19px}
  .icon-question{width:20px;height:20px;border-radius:50%;background:var(--white);color:var(--red);font-size:14px;font-weight:800;display:inline-flex;align-items:center;justify-content:center}
  .who p{margin-top:12px;font-size:13.2px;line-height:17.5px;color:var(--pale)}
  .who p:first-of-type{margin-top:14px}

  /* services */
  .services{left:0;top:617px;width:423px;height:436px;padding:24px 30px 0}
  .services h2{font-size:19px;font-weight:800;line-height:21px;color:var(--ink)}
  .service-list{list-style:none;margin-top:16px}
  .service-list li{display:flex;align-items:flex-start;gap:14px;font-size:13.4px;line-height:18px;min-height:28px}
  .service-list li.two-line{min-height:47px}
  .service-list .icon{width:19px;height:19px}

  /* why choose */
  .why-edge{left:843px;top:387px;width:9px;height:230px;background:var(--red)}
  .why{left:423px;top:387px;width:420px;height:654px;background:var(--black);padding:19px 28px 0;color:var(--white)}
  .why h2{font-size:19px;font-weight:700;line-height:1}
  .reason{margin-top:24px}
  .reason h3{display:flex;align-items:flex-start;gap:14px;font-size:17px;font-weight:500;color:var(--red-text);line-height:21px;letter-spacing:.3px}
  .reason h3 .icon{margin-top:1px}
  .reason p{margin-top:14px;font-size:13.4px;line-height:17.5px}

  /* footer */
  .contact{left:0;top:1053px;width:423px;height:130px;background:var(--black);padding:20px 30px 0;color:var(--white)}
  .licenses{left:423px;top:1053px;width:429px;height:147px;background:var(--red);padding:20px 28px 0;color:var(--white)}
  .footer-head{font-size:17px;font-weight:700;line-height:1}
  .contact .footer-head em{font-style:normal;color:var(--red-text)}
  .licenses .footer-head em{font-style:normal;color:var(--ink)}
  .detail-row{display:flex;align-items:center;gap:12px;margin-top:10px;font-size:13.4px;line-height:18px}
  .detail-row .gap{width:8px}
  .licenses .detail-row strong{font-weight:700}
  .icon-light{width:19px;height:19px;border-radius:50%;background:var(--white);flex:none;display:inline-flex;align-items:center;justify-content:center}
  .icon-red{width:19px;height:19px;border-radius:50%;background:var(--red);flex:none;display:inline-flex;align-items:center;justify-content:center}
  .divider{opacity:.8}
</style>
</head>
<body>
<div class="sheet">

  <div class="block hero-photo" role="img" aria-label="Photograph of hanging glowing filament light bulbs against a dark background"></div>

  <svg class="block hero-shapes" viewBox="0 0 852 390" aria-hidden="true">
    <polygon points="0,0 312,0 414,173 300,377 0,377" fill="#ffffff"/>
    <polygon points="0,0 297,0 400,173 285,377 0,377" fill="#1b1b1b"/>
    <rect x="300" y="293" width="552" height="97" fill="#ffffff"/>
    <polygon points="352,293 852,293 852,306 372,306 324,361 303,361" fill="#b8382f"/>
  </svg>

  <div class="block brand">
    <div class="brand-name"><span class="brand-dot"></span>BrightWire Pro</div>
    <div class="brand-rule"></div>
  </div>

  <div class="block intro mission">
    <div class="section-head"><span class="icon"></span>OUR <em>MISSION</em></div>
    <p>Dedicate ourselves to providing world class service to anyone in need, based on honesty, communication and respect.</p>
  </div>

  <div class="block intro values">
    <div class="section-head"><span class="icon"></span>CORE <em>VALUES</em></div>
    <p>Safety and Security is priority<br>Support when you need it most<br>Service with an over-the-top WOW<br>Satisfaction with loyalty and integrity</p>
  </div>

  <div class="block statement-title">CAPABILITIES <strong>STATEMENT</strong></div>

  <section class="block who">
    <div class="section-head"><span class="icon-question">?</span>WHO WE ARE</div>
    <p>BrightWire Pro is a growing Electrical maintenance company based in the Inner West.</p>
    <p>We are established on sound service principles with honesty, communication, and respect at the forefront of every team member.</p>
    <p>We strive for openness, trust, and accountability and we are in the business of providing solutions to help others. We see ourselves as an extension of your team.</p>
  </section>

  <section class="block services">
    <h2>Brief List of the most common<br>services we provide</h2>
    <ul class="service-list">
      <li><span class="icon"></span>24/7 Emergency service</li>
      <li><span class="icon"></span>Switchboard UPGRADE and REPAIRS</li>
      <li><span class="icon"></span>Light fitting installations</li>
      <li><span class="icon"></span>Powerpoint installations</li>
      <li><span class="icon"></span>Surge device installations</li>
      <li><span class="icon"></span>Testing and servicing electric hot water systems</li>
      <li><span class="icon"></span>Smoke Alarm installation with compliance certificate</li>
      <li><span class="icon"></span>Electric Vehicle charging stations</li>
      <li class="two-line"><span class="icon"></span>Ceiling and Exhaust fan installations with<br>roof and wall venting</li>
      <li><span class="icon"></span>Appliance installations</li>
      <li><span class="icon"></span>Fault finding</li>
      <li><span class="icon"></span>TV, DATA and FREE TO AIR Aerial installations</li>
    </ul>
  </section>

  <div class="block why-edge"></div>
  <section class="block why">
    <h2>WHY CHOOSE BRIGHTWIRE PRO</h2>
    <div class="reason">
      <h3><span class="icon"></span>Support when you need it most</h3>
      <p>BrightWire provides around the clock assistance, whether during normal business hours or emergencies we are focused on providing solutions for our clients.</p>
    </div>
    <div class="reason">
      <h3><span class="icon"></span>Fast and responsive team with a<br>direct contact</h3>
      <p>BrightWire treats every one of our clients as a VIP. We pride ourselves on being able to provide a quick turn around for all our jobs. We make the whole process smooth, from booking the job to attending and completion.</p>
    </div>
    <div class="reason">
      <h3><span class="icon"></span>Satisfaction with loyalty and integrity</h3>
      <p>We value our transparency and communication skills to deliver an outstanding performance which reflects our happy customer base.</p>
    </div>
    <div class="reason">
      <h3><span class="icon"></span>We provide courtesy calls</h3>
      <p>The appointment will be confirmed the day before and our technicians will call you half an hour in advance on approach to the job</p>
    </div>
    <div class="reason">
      <h3><span class="icon"></span>Licensed and insured technicians</h3>
      <p>All our technicians are experts of their field, with the relevant equipment, knowledge and licenses to carry out our duties.</p>
    </div>
  </section>

  <section class="block contact">
    <div class="footer-head">CONTACT <em>DETAILS</em></div>
    <div class="detail-row">
      <span class="icon-red"><svg width="11" height="11" viewBox="0 0 24 24"><path fill="#fff" d="M6.6 10.8a15 15 0 0 0 6.6 6.6l2.2-2.2c.3-.3.7-.4 1-.2 1.1.4 2.3.6 3.6.6.6 0 1 .4 1 1V20c0 .6-.4 1-1 1A17 17 0 0 1 3 4c0-.6.4-1 1-1h3.5c.6 0 1 .4 1 1 0 1.3.2 2.5.6 3.6.1.3 0 .7-.2 1z"/></svg></span>
      Daniel - 0400 118 203<span class="gap"></span>
      <span class="icon-red"><svg width="11" height="11" viewBox="0 0 24 24"><path fill="#fff" d="M6.6 10.8a15 15 0 0 0 6.6 6.6l2.2-2.2c.3-.3.7-.4 1-.2 1.1.4 2.3.6 3.6.6.6 0 1 .4 1 1V20c0 .6-.4 1-1 1A17 17 0 0 1 3 4c0-.6.4-1 1-1h3.5c.6 0 1 .4 1 1 0 1.3.2 2.5.6 3.6.1.3 0 .7-.2 1z"/></svg></span>
      Marcus - 0400 226 914
    </div>
    <div class="detail-row">
      <span class="icon-red"><svg width="11" height="11" viewBox="0 0 24 24"><path fill="none" stroke="#fff" stroke-width="2.4" d="M3 6h18v12H3zM3 6l9 7 9-7"/></svg></span>
      services@brightwirepro.com.au
    </div>
    <div class="detail-row">
      <span class="icon-red"><svg width="11" height="11" viewBox="0 0 24 24"><g fill="none" stroke="#fff" stroke-width="2"><circle cx="12" cy="12" r="9"/><path d="M3 12h18M12 3c3 3 3 15 0 18M12 3c-3 3-3 15 0 18"/></g></svg></span>
      brightwirepro.com.au/index.html
    </div>
  </section>

  <section class="block licenses">
    <div class="footer-head">LICENSES <em>DETAILS</em></div>
    <div class="detail-row">Electrical license number BrightWire Pro Pty Ltd - 451276C</div>
    <div class="detail-row">
      <span class="icon-light"><svg width="11" height="11" viewBox="0 0 24 24"><path fill="none" stroke="#b8382f" stroke-width="3" d="M4 12l5 5L20 6"/></svg></span>
      Daniel - 318462C<span class="gap"></span>
      <span class="icon-light"><svg width="11" height="11" viewBox="0 0 24 24"><path fill="none" stroke="#b8382f" stroke-width="3" d="M4 12l5 5L20 6"/></svg></span>
      Marcus - 417390C
    </div>
    <div class="detail-row">
      <span class="icon-light"><svg width="11" height="11" viewBox="0 0 24 24"><path fill="none" stroke="#b8382f" stroke-width="2.4" d="M5 3h10l4 4v14H5z"/></svg></span>
      <strong>ABN: 5128 4407 316</strong><span class="divider">|</span><strong>Public Liability $20,000,000</strong>
    </div>
  </section>

</div>
</body>
</html>
```